Pelican Litigation Funding Letterhead & Document Template

We need a letter head designed for our fund. Our fund works with law firms and investors across the globe. We need a a cover letter template as well as a document template for subsequent pages. Blue and white color scheme is preferred. This is our predecessor's website: https://www.pelicanvq.com/index.html. Please see our logo attached. The logo color code is #19478d. Font is Gotham-Medium.
Target Market(s)
Sophisticated investors and law firms
Font styles to use
Sans Serif
Colors
0255a3

```html
<!DOCTYPE html>
<html lang="en">
<head>
<meta charset="utf-8">
<title>Pelican Litigation Funding — Letterhead</title>
<link rel="stylesheet" href="https://fonts.googleapis.com/css2?family=Lato:wght@400&display=swap">
<style>
  :root {
    --brand-blue: #15488b;
    --band-grey: #b3b3b3;
    --backdrop: #d6d6d6;
    --paper: #ffffff;
    --ink: #3a3a3a;
  }
  html, body {
    margin: 0;
    padding: 0;
    width: 1056px;
    height: 1200px;
    overflow: hidden;
    background: var(--backdrop);
  }
  .letterhead {
    position: absolute;
    left: 104px;
    top: 0;
    width: 848px;
    height: 1200px;
    background: var(--paper);
    overflow: hidden;
  }
  .side-band {
    position: absolute;
    left: 0;
    top: 0;
    width: 41px;
    height: 1200px;
  }
  .company-name {
    position: absolute;
    left: 41px;
    right: 0;
    top: 112px;
    margin: 0;
    text-align: center;
    font-family: "Lato", sans-serif;
    font-weight: 400;
    font-size: 28px;
    line-height: 34px;
    color: var(--brand-blue);
  }
  .contact-frame {
    position: absolute;
    left: 20px;
    top: 1014px;
    width: 35px;
    height: 152px;
  }
  .contact-list {
    position: absolute;
    left: 64px;
    top: 1026px;
    margin: 0;
    padding: 0;
    list-style: none;
    font-family: "Lato", sans-serif;
    font-weight: 400;
    font-size: 17px;
    line-height: 21px;
    color: var(--ink);
  }
  .contact-list li { margin: 0; }
  .contact-list .address { margin-bottom: 20px; }
  .contact-list .web-domain { color: var(--brand-blue); }
</style>
</head>
<body>
  <main class="letterhead">
    <svg class="side-band" viewBox="0 0 41 1200" aria-hidden="true">
      <polygon points="0,0 41,0 41,317 0,295" fill="var(--band-grey)"/>
      <polygon points="0,307 41,330 41,1200 0,1200" fill="var(--brand-blue)"/>
    </svg>

    <h1 class="company-name">Pelican Litigation Funding</h1>

    <svg class="contact-frame" viewBox="0 0 35 152" aria-hidden="true">
      <rect x="1.5" y="1.5" width="33" height="149" fill="var(--brand-blue)"/>
      <path d="M1.5 1.5 V150.5 M1.5 1.5 H35 M1.5 150.5 H35" stroke="#fff" stroke-width="3" fill="none"/>
      <path d="M21 20 c-4.4 0 -7.5 3.2 -7.5 7.3 c0 5 7.5 11.7 7.5 11.7 s7.5 -6.7 7.5 -11.7 c0 -4.1 -3.1 -7.3 -7.5 -7.3 z" fill="#fff"/>
      <circle cx="21" cy="27.3" r="2.6" fill="var(--brand-blue)"/>
      <path d="M15 80 c1 -1 2.5 -1 3.2 0 l1.6 2.2 c0.6 0.8 0.4 1.9 -0.4 2.5 l-1 0.7 c0.8 1.8 2.2 3.2 4 4 l0.7 -1 c0.6 -0.8 1.7 -1 2.5 -0.4 l2.2 1.6 c1 0.7 1 2.2 0 3.2 l-1 1 c-1.3 1.3 -3.3 1.4 -4.9 0.4 c-3.3 -2 -5.9 -4.6 -7.9 -7.9 c-1 -1.6 -0.9 -3.6 0.4 -4.9 z" fill="#fff"/>
      <path d="M22 79 a6 6 0 0 1 5 5 M22 75.5 a9.5 9.5 0 0 1 8.5 8.5" stroke="#fff" stroke-width="1.3" fill="none"/>
      <rect x="13.5" y="104" width="15" height="10.5" fill="none" stroke="#fff" stroke-width="1.4"/>
      <path d="M13.5 104 L21 110 L28.5 104 M13.5 114.5 L19 109 M28.5 114.5 L23 109" stroke="#fff" stroke-width="1.2" fill="none"/>
      <circle cx="21" cy="133" r="7" fill="none" stroke="#fff" stroke-width="1.3"/>
      <ellipse cx="21" cy="133" rx="3" ry="7" fill="none" stroke="#fff" stroke-width="1"/>
      <path d="M14 133 H28 M15 129.5 H27 M15 136.5 H27" stroke="#fff" stroke-width="1"/>
    </svg>

    <ul class="contact-list">
      <li class="address">1234 First Line Address<br>5678 Second Line Address</li>
      <li class="phone">(111) 999-0000</li>
      <li class="email">Info@yourmail.com</li>
      <li class="website">www.<span class="web-domain">yourwebsite</span>.com</li>
    </ul>
  </main>
</body>
</html>
```